BrightLoopDeals

I need 4 thumbnails for the website area "How It Works". Sizes of thumbnails should be 400x290px. Something that reflects the steps and suits the rest of the site brightloopdeals.com design

```html
<!DOCTYPE html>
<html lang="en">
<head>
<meta charset="utf-8">
<title>BrightLoopDeals — How It Works</title>
<link rel="stylesheet" href="https://fonts.googleapis.com/css2?family=Lexend:wght@500&family=Inter:wght@400&display=swap">
<style>
  :root {
    --page-bg: #f9fafd;
    --frame-border: #5a1a55;
    --plum-deep: #42053d;
    --plum-mid: #7a2872;
    --plum-light: #c77cc6;
    --icon-soft: #f1d6f0;
    --icon-accent: #d98fd7;
    --icon-dark: #3a3f47;
    --heading: #151515;
    --body-text: #8d8d8d;
    --badge-bg: #ffffff;
  }
  html, body {
    margin: 0;
    padding: 0;
    width: 1200px;
    height: 427px;
    overflow: hidden;
    background: var(--page-bg);
  }
  .how-it-works {
    position: absolute;
    left: 29px;
    top: 36px;
    width: 1142px;
    height: 357px;
    box-sizing: border-box;
    border: 1.2px solid var(--frame-border);
    border-radius: 24px;
  }
  .steps {
    position: absolute;
    left: 23px;
    top: 24px;
    display: grid;
    grid-template-columns: repeat(4, 264px);
    column-gap: 13px;
  }
  .step { position: relative; }
  .step-thumb {
    position: relative;
    width: 264px;
    height: 191px;
    border-radius: 14px;
    overflow: hidden;
    background: linear-gradient(180deg, var(--plum-deep) 0%, var(--plum-mid) 55%, var(--plum-light) 100%);
  }
  .step-icon {
    position: absolute;
    left: 0;
    top: 0;
    width: 264px;
    height: 191px;
  }
  .step-number {
    position: absolute;
    left: 118px;
    top: 177px;
    width: 28px;
    height: 28px;
    border-radius: 50%;
    background: var(--badge-bg);
    box-shadow: 0 2px 5px rgba(0,0,0,0.18);
    display: flex;
    align-items: center;
    justify-content: center;
    font-family: 'Inter', sans-serif;
    font-size: 12px;
    color: var(--heading);
  }
  .step-title {
    margin: 26px 0 0 3px;
    font-family: 'Lexend', sans-serif;
    font-weight: 500;
    font-size: 15.4px;
    line-height: 20px;
    color: var(--heading);
    white-space: nowrap;
  }
  .step-text {
    margin: 6px 0 0 3px;
    width: 272px;
    font-family: 'Inter', sans-serif;
    font-size: 10.9px;
    line-height: 16.4px;
    color: var(--body-text);
  }
</style>
</head>
<body>
  <section class="how-it-works">
    <div class="steps">
      <article class="step">
        <div class="step-thumb" role="img" aria-label="Illustration of a person beside a large tablet showing a sign-in form, with a lock icon and a key">
          <svg class="step-icon" viewBox="0 0 264 191" aria-hidden="true">
            <ellipse cx="132" cy="170" rx="150" ry="60" fill="#ffffff" opacity="0.08"/>
            <rect x="92" y="48" width="80" height="98" rx="8" fill="var(--icon-dark)"/>
            <rect x="98" y="54" width="68" height="86" rx="4" fill="var(--icon-soft)"/>
            <rect x="112" y="88" width="40" height="30" rx="4" fill="var(--icon-accent)"/>
            <path d="M120 88 v-8 a12 12 0 0 1 24 0 v8" fill="none" stroke="var(--icon-accent)" stroke-width="4"/>
            <circle cx="132" cy="101" r="4" fill="var(--icon-soft)"/>
            <rect x="130" y="103" width="4" height="8" fill="var(--icon-soft)"/>
            <rect x="108" y="126" width="48" height="8" rx="4" fill="var(--icon-accent)"/>
          </svg>
        </div>
        <div class="step-number">1</div>
        <h3 class="step-title">Create an account</h3>
        <p class="step-text">Content creator or a sponsor, it's as easy as 1-2-3 to create your account and describe what you are looking for. You are 3 steps away from getting your promo deal done.</p>
      </article>
      <article class="step">
        <div class="step-thumb" role="img" aria-label="Illustration of a person with a laptop in a bean bag next to a large search window and web address tags">
          <svg class="step-icon" viewBox="0 0 264 191" aria-hidden="true">
            <ellipse cx="132" cy="170" rx="150" ry="60" fill="#ffffff" opacity="0.08"/>
            <rect x="70" y="42" width="124" height="100" rx="8" fill="var(--icon-soft)"/>
            <rect x="70" y="42" width="124" height="18" rx="8" fill="var(--icon-accent)"/>
            <rect x="80" y="48" width="70" height="6" rx="3" fill="var(--icon-soft)"/>
            <circle cx="124" cy="96" r="20" fill="none" stroke="var(--icon-dark)" stroke-width="6"/>
            <line x1="139" y1="111" x2="158" y2="130" stroke="var(--icon-dark)" stroke-width="8" stroke-linecap="round"/>
          </svg>
        </div>
        <div class="step-number">2</div>
        <h3 class="step-title">Find the right promo match</h3>
        <p class="step-text">Search for multi-platform opportunities to place your advertisement and promote a product. It's a win-win opportunity to promote a product the best way.</p>
      </article>
      <article class="step">
        <div class="step-thumb" role="img" aria-label="Illustration of two people discussing a large screen with design panels, charts and settings gears">
          <svg class="step-icon" viewBox="0 0 264 191" aria-hidden="true">
            <ellipse cx="132" cy="170" rx="150" ry="60" fill="#ffffff" opacity="0.08"/>
            <path d="M70 50 h86 a8 8 0 0 1 8 8 v44 a8 8 0 0 1 -8 8 h-50 l-18 16 v-16 h-18 a8 8 0 0 1 -8 -8 v-44 a8 8 0 0 1 8 -8 z" fill="var(--icon-soft)"/>
            <rect x="84" y="66" width="62" height="6" rx="3" fill="var(--icon-accent)"/>
            <rect x="84" y="80" width="46" height="6" rx="3" fill="var(--icon-accent)"/>
            <path d="M124 82 h64 a8 8 0 0 1 8 8 v36 a8 8 0 0 1 -8 8 h-12 v14 l-16 -14 h-36 a8 8 0 0 1 -8 -8 v-36 a8 8 0 0 1 8 -8 z" fill="var(--icon-dark)"/>
            <circle cx="142" cy="108" r="4" fill="var(--icon-soft)"/>
            <circle cx="156" cy="108" r="4" fill="var(--icon-soft)"/>
            <circle cx="170" cy="108" r="4" fill="var(--icon-soft)"/>
          </svg>
        </div>
        <div class="step-number">3</div>
        <h3 class="step-title">Discuss all the details</h3>
        <p class="step-text">Find multiple opportunities and decide on the best one to execute a successful promo campaign.</p>
      </article>
      <article class="step">
        <div class="step-thumb" role="img" aria-label="Illustration of a person choosing team members from profile cards under a My Team board">
          <svg class="step-icon" viewBox="0 0 264 191" aria-hidden="true">
            <ellipse cx="132" cy="170" rx="150" ry="60" fill="#ffffff" opacity="0.08"/>
            <rect x="84" y="40" width="96" height="112" rx="8" fill="var(--icon-soft)"/>
            <rect x="112" y="32" width="40" height="16" rx="4" fill="var(--icon-dark)"/>
            <rect x="98" y="62" width="68" height="6" rx="3" fill="var(--icon-accent)"/>
            <rect x="98" y="76" width="50" height="6" rx="3" fill="var(--icon-accent)"/>
            <circle cx="132" cy="114" r="22" fill="var(--icon-accent)"/>
            <path d="M120 114 l8 8 l16 -16" fill="none" stroke="#ffffff" stroke-width="6" stroke-linecap="round" stroke-linejoin="round"/>
          </svg>
        </div>
        <div class="step-number">4</div>
        <h3 class="step-title">Get the deal done</h3>
        <p class="step-text">You decide who you work with. Choose what works best for you and your product.</p>
      </article>
    </div>
  </section>
</body>
</html>
```